Velta Harbor Solutions

I have a file with a logo. It is grainy. I also have a board with my color pallet and other branding items. I need a file with the logo that is high resolution and I also need a business card design.

```html
<!DOCTYPE html>
<html lang="en">
<head>
<meta charset="utf-8">
<title>Velta Harbor Solutions – Business Card</title>
<link href="https://fonts.googleapis.com/css2?family=Source+Sans+3:ital,wght@0,300;0,400;0,700;1,400;1,700&display=swap" rel="stylesheet">
<style>
  :root {
    --canvas: #ffffff;
    --navy-card: #282d37;
    --linen-card: #ebe5e3;
    --ink: #2c3548;
    --white: #ffffff;
    --arrow-red: #961a22;
    --sand: #ddd0c6;
    --deep-navy: #2e3a4f;
    --slate: #4a5a70;
    --fog: #6b7b8c;
    --charcoal: #363b45;
  }
  html, body {
    margin: 0;
    padding: 0;
    width: 1200px;
    height: 1200px;
    overflow: hidden;
    background: var(--canvas);
    font-family: "Source Sans 3", sans-serif;
  }
  .canvas {
    position: relative;
    width: 1200px;
    height: 1200px;
  }
  .card {
    position: absolute;
    left: 238px;
    width: 733px;
    height: 390px;
    overflow: hidden;
  }
  .card--front { top: 166px; background: var(--navy-card); }
  .card--back  { top: 592px; background: var(--linen-card); color: var(--ink); }
  .card__artwork {
    position: absolute;
    right: 0;
    top: 8px;
    bottom: 8px;
    width: 230px;
    background: linear-gradient(165deg, var(--sand) 0%, var(--fog) 35%, var(--slate) 60%, var(--charcoal) 100%);
  }
  .card__artwork::before {
    content: "";
    position: absolute;
    inset: 0;
    background: linear-gradient(90deg, rgba(150, 26, 34, 0.35) 0%, rgba(150, 26, 34, 0) 45%);
  }
  .brand-name {
    position: absolute;
    left: 82px;
    top: 150px;
    width: 300px;
    margin: 0;
    text-align: center;
    color: var(--white);
    font-weight: 700;
    font-size: 40px;
    line-height: 1.05;
    letter-spacing: 0.5px;
  }
  .person {
    position: absolute;
    left: 106px;
    top: 56px;
    width: 300px;
    text-align: center;
  }
  .person__name {
    margin: 0;
    font-weight: 300;
    font-size: 42px;
    line-height: 1.1;
    letter-spacing: 0.5px;
  }
  .person__role {
    margin: 0;
    font-weight: 700;
    font-style: italic;
    font-size: 29px;
    line-height: 1.1;
  }
  .contact-list {
    position: absolute;
    left: 106px;
    top: 162px;
    margin: 0;
    padding: 0;
    list-style: none;
  }
  .contact-list__item {
    display: flex;
    align-items: center;
    height: 40px;
    margin-bottom: 24px;
    font-style: italic;
    font-size: 24px;
  }
  .contact-list__item:nth-child(2) { margin-bottom: 26px; }
  .contact-list__icon {
    width: 44px;
    height: 40px;
    margin-right: 16px;
    fill: var(--ink);
  }
</style>
</head>
<body>
<main class="canvas">

  <section class="card card--front" aria-label="Business card front">
    <div class="card__artwork" role="img" aria-label="Brand graphic of an upward red arrow crossing stepped colour bars"></div>
    <h1 class="brand-name">Velta Harbor<br>Solutions</h1>
  </section>

  <section class="card card--back" aria-label="Business card back">
    <div class="card__artwork" role="img" aria-label="Brand graphic of an upward red arrow crossing stepped colour bars"></div>

    <div class="person">
      <h2 class="person__name">Daniel Carver</h2>
      <p class="person__role">Manager</p>
    </div>

    <ul class="contact-list">
      <li class="contact-list__item">
        <svg class="contact-list__icon" viewBox="0 0 44 40" aria-hidden="true">
          <path d="M2 6h40v28H2z M6 9l16 13L38 9H6z M5 12v19l11-10z M39 12L28 21l11 10z M18 23l-11 9h30L26 23l-4 3z" fill-rule="evenodd"/>
        </svg>
        <span>hello@veltaharbor.com</span>
      </li>
      <li class="contact-list__item">
        <svg class="contact-list__icon" viewBox="0 0 44 40" aria-hidden="true">
          <circle cx="22" cy="20" r="17"/>
          <g fill="var(--linen-card)">
            <circle cx="22" cy="20" r="4"/>
            <circle cx="12" cy="12" r="3"/>
            <circle cx="32" cy="13" r="3"/>
            <circle cx="13" cy="29" r="3"/>
            <circle cx="30" cy="30" r="3"/>
          </g>
          <g stroke="var(--linen-card)" stroke-width="1.5">
            <line x1="12" y1="12" x2="22" y2="20"/>
            <line x1="32" y1="13" x2="22" y2="20"/>
            <line x1="13" y1="29" x2="22" y2="20"/>
            <line x1="30" y1="30" x2="22" y2="20"/>
          </g>
        </svg>
        <span>www.veltaharbor.com</span>
      </li>
      <li class="contact-list__item">
        <svg class="contact-list__icon" viewBox="0 0 44 48" aria-hidden="true">
          <path d="M22 2C12 2 5 9 5 18c0 11 17 28 17 28s17-17 17-28C39 9 32 2 22 2zm0 23a7 7 0 1 1 0-14 7 7 0 0 1 0 14z"/>
        </svg>
        <span>Easton, 216 street, NY</span>
      </li>
    </ul>
  </section>

</main>
</body>
</html>
```